Business Card Design for Real Estate Company

I am looking for a business card design that will catch my client's attention.

Industry/Entity Type

Business

Requirements
Must have
• Please have the following information in the business card design. You can substitute the "Office, Mobile, email, and web" with an icon or some other design you may think will go well with the business card.

Toma Verdi
482 W. Orchard Blvd., Suite 300
Pasadena, CA 91187
Office: 626.555.0147
Mobile: 626.555.0193
email: Toma@QuillStoneEstates.example
web: www.QuillStoneEstates.example

```html
<!DOCTYPE html>
<html lang="en">
<head>
<meta charset="utf-8">
<title>QuillStone Estates – Business Card</title>
<link rel="stylesheet" href="https://fonts.googleapis.com/css2?family=Arimo:wght@400&display=swap">
<style>
  :root {
    --page-bg: #f4f4f2;
    --card-white: #ffffff;
    --card-edge: #2a2a2a;
    --ink: #1c1c1c;
    --ink-soft: #333333;
    --leaf-teal: #6f8f8c;
    --leaf-grey: #a9b2b1;
    --leaf-blue: #3fa0dc;
    --back-center: #ffffff;
    --back-edge: #b9b9b9;
    --mark-dot: #4a9a6a;
  }
  * { box-sizing: border-box; margin: 0; padding: 0; }
  html, body {
    width: 1200px; height: 483px; overflow: hidden;
    background: var(--page-bg);
    font-family: "Arimo", Arial, sans-serif;
    color: var(--ink);
  }
  .card-set {
    position: absolute; top: 99px; left: 92px;
    display: flex; gap: 20px;
  }
  .card {
    position: relative;
    width: 498px; height: 285px;
    border: 1.5px solid var(--card-edge);
    overflow: hidden;
  }
  /* Front */
  .card-front { background: var(--card-white); }
  .front-artwork {
    position: absolute; left: 0; top: 0;
    width: 168px; height: 100%;
    background: linear-gradient(160deg, var(--leaf-grey) 0%, var(--leaf-teal) 55%, var(--leaf-blue) 100%);
    opacity: 0.55;
  }
  .front-details {
    position: absolute; right: 34px; top: 36px;
    text-align: right;
  }
  .holder-name {
    font-size: 35px; font-weight: 400; line-height: 1.2;
    margin-bottom: 10px;
  }
  .contact-lines, .address-lines {
    font-size: 15.5px; line-height: 19px; color: var(--ink-soft);
  }
  .address-lines { margin-top: 13px; }
  .front-brand {
    position: absolute; right: 34px; top: 222px;
    font-size: 27px; color: var(--ink);
  }
  /* Back */
  .card-back {
    background: radial-gradient(ellipse at 50% 45%, var(--back-center) 0%, #e6e6e6 45%, var(--back-edge) 100%);
    text-align: center;
  }
  .brand-dot {
    position: absolute; left: 50%; top: 56px;
    width: 44px; height: 44px; margin-left: -22px;
    border-radius: 50%; background: var(--mark-dot);
  }
  .back-brand {
    position: absolute; left: 0; right: 0; top: 134px;
    font-size: 40px; color: var(--ink);
  }
  .back-web {
    position: absolute; left: 0; right: 0; top: 196px;
    font-size: 16px; color: var(--ink-soft);
  }
</style>
</head>
<body>
  <main class="card-set">
    <section class="card card-front">
      <div class="front-artwork" role="img" aria-label="Decorative tree with teal, grey and blue leaves"></div>
      <div class="front-details">
        <h1 class="holder-name">Toma Verdi</h1>
        <p class="contact-lines">
          Office: 626.555.0147<br>
          Mobile: 626.555.0193<br>
          Toma@QuillStoneEstates.example
        </p>
        <p class="address-lines">
          482 W. Orchard Blvd., Suite 300<br>
          Pasadena, CA 91187
        </p>
      </div>
      <p class="front-brand">QuillStone Estates</p>
    </section>

    <section class="card card-back">
      <span class="brand-dot" aria-hidden="true"></span>
      <p class="back-brand">QuillStone Estates</p>
      <p class="back-web">www.QuillStoneEstates.example</p>
    </section>
  </main>
</body>
</html>
```